WeatheredIt.net wordpress design

Concept: Website where personal stories, personal videos can be posted as a challenge while awaiting the wisdom of experience from others who have WeatheredIt same event or challenge in their lifetime.
Support aspects will be in 4 quadrants of Challenges:
1. Financial 2. Medical & Physical
3. Legal Matters 4. Psychological & Spiritual - ability to chat online with a spiritual/psychological counselor or life coach
Updates
Project Deadline Extended
Reason: Bit more time to complete designs.
Wanted to thank all of you for your designs! Greatly appreciated. Very creative ideas that captured the essence of this website. Will be back with a selection very shortly.
Target Market(s)
Anyone looking for a solution based upon experiential wisdom
Industry/Entity Type
Financial
Requirements
Must have
- Interactive website: Where you can post a challenge or issue via a written question or a video and ask for a solution.
Ability to access any of the 4 Quadrants (as listed above) to ask for an expert, via experience, advice and wisdom from those who have similar challenges.

```html
<!DOCTYPE html>
<html lang="en">
<head>
<meta charset="utf-8">
<title>WeatheredIt.net</title>
<link rel="stylesheet" href="https://fonts.googleapis.com/css2?family=Didact+Gothic&family=Poppins:wght@500;600&display=swap">
<style>
:root{
  --blue-deep:#1d3f6b;
  --blue-mid:#3a6a9c;
  --orange:#f5a400;
  --gold:#d99a12;
  --ink:#1b1b1b;
  --text:#555;
  --muted:#777;
  --field-border:#cfcfcf;
  --btn:#1c1c1c;
  --pill:#8a8a8a;
  --page:#dedede;
  --white:#fff;
}
*{box-sizing:border-box;margin:0;padding:0}
html,body{width:1158px;height:1200px;overflow:hidden}
body{position:relative;background:var(--page);background-image:radial-gradient(#d2d2d2 1px,transparent 1.2px);background-size:4px 4px;font-family:"Didact Gothic",sans-serif;color:var(--text)}
.top-band{position:absolute;left:0;top:0;width:1158px;height:482px;background:linear-gradient(90deg,var(--blue-deep),var(--blue-mid) 4%,var(--blue-mid) 96%,var(--blue-deep));border-top:3px solid var(--orange)}
.hero-photo{position:absolute;left:73px;top:3px;width:1047px;height:459px;background:linear-gradient(100deg,#f4f1ec 0%,#e9ddc8 22%,#d6b88a 34%,#efe9e0 48%,#f7f7f5 70%,#eeeeec 100%)}
.nav{position:absolute;left:137px;top:3px;width:916px;height:30px;background:var(--white);border-radius:0 0 3px 3px;box-shadow:0 1px 3px rgba(0,0,0,.15);display:flex;align-items:center}
.nav a{color:#444;text-decoration:none;font-size:15px;padding:0 25px;border-right:1px solid #ccc;line-height:20px}
.nav a.current{color:var(--ink);font-family:"Poppins",sans-serif;font-weight:600;font-size:14px;padding-left:20px}
.nav a:nth-child(4){border-right:0}
.account{position:absolute;right:186px;top:8px;font-family:"Poppins",sans-serif;font-weight:600;font-size:10.5px;color:var(--ink);line-height:14px}
.account span{text-decoration:underline;margin:0 7px}
.search{position:absolute;right:7px;top:5px;width:171px;height:19px;border:1px solid #999;display:flex}
.search input{flex:1;border:0;font:italic 11px "Didact Gothic",sans-serif;padding-left:5px;color:#aaa;min-width:0}
.search b{width:24px;background:var(--btn);color:#fff;font:600 12px "Poppins",sans-serif;text-align:center;line-height:19px}
.brand{position:absolute;left:140px;top:64px;width:128px;height:56px;background:rgba(255,255,255,.88);display:flex;align-items:center;gap:6px;padding-left:8px;font-family:"Poppins",sans-serif;font-weight:600;font-size:15px;color:var(--gold)}
.brand i{width:14px;height:14px;background:var(--orange);display:block}
.slogan{position:absolute;left:481px;top:372px;color:#222}
.slogan h1{font-weight:400;font-size:27px;line-height:30px}
.slogan h1 strong{font-family:"Poppins",sans-serif;font-weight:600}
.slogan p{font-size:15px;margin-top:-1px}
.dots{position:absolute;left:137px;top:433px;display:flex;gap:5px;align-items:center}
.dots span{width:8px;height:8px;border-radius:50%;background:var(--blue-deep)}
.dots span:first-child{width:12px;height:12px;border:2px solid var(--blue-deep);background:#fff}
.ask{position:absolute;left:789px;top:63px;width:264px;height:367px;background:var(--white);border-radius:3px;box-shadow:0 1px 6px rgba(0,0,0,.2);padding:30px 12px 0 13px}
.ask h2{font-weight:400;font-size:21px;color:#333}
.ask p{font-size:13px;line-height:15px;margin:6px 0 18px;color:#555}
.field{border:1px solid var(--field-border);border-radius:4px;height:26px;margin-bottom:4px;font-size:13px;color:#aaa;padding:4px 6px}
.field.tall{height:104px}
.row{display:flex;gap:4px}
.row .field:first-child{flex:1}
.row .field:last-child{width:72px;text-align:center;background:#f6f6f6}
.btn{display:block;background:var(--btn);color:#fff;font:600 12.5px "Poppins",sans-serif;text-align:center;border-radius:3px;height:25px;line-height:25px}
.content{position:absolute;left:137px;top:462px;width:916px;height:699px;background:var(--white);border-radius:0 0 3px 3px}
.section-title{position:absolute;font-weight:400;font-size:20px;color:#333}
.rule{position:absolute;height:10px;background:radial-gradient(ellipse at top,rgba(0,0,0,.13),transparent 70%)}
.article{position:absolute;left:17px;width:410px}
.article h3,.quad h3{font-family:"Poppins",sans-serif;font-weight:500;color:var(--ink)}
.article h3{font-size:14px;line-height:16px}
.meta{font-family:"Poppins",sans-serif;font-weight:500;font-size:10px;color:var(--gold);line-height:13px}
.share{display:flex;gap:2px;margin:3px 0 4px}
.share i{width:16px;height:16px;border-radius:2px;display:block}
.share i:nth-child(1),.share i:nth-child(2){background:#f08a24}
.share i:nth-child(3){background:#3d5c98}
.share i:nth-child(4){background:#c9d6e2}
.share i:nth-child(5){background:#3aaee0}
.share i:nth-child(6){background:#e5508a}
.article p{font-size:11.5px;line-height:14px;color:#555;width:405px}
.more{display:inline-block;background:var(--pill);color:#fff;font-size:11px;line-height:15px;padding:0 8px;border-radius:4px;margin-top:3px;box-shadow:inset 0 1px 0 #aaa}
.quad{position:absolute;width:200px}
.quad h3{font-size:16px;line-height:20px;margin-bottom:8px}
.entry{margin-bottom:7px;font-size:11.5px;line-height:14px;color:var(--muted)}
.entry b{font-family:"Poppins",sans-serif;font-weight:500;font-size:11px;color:#555;display:block}
.chat{position:absolute;left:525px;top:560px;width:260px}
.chat h2{font-weight:400;font-size:20px;line-height:24px;color:#333}
.chat p{font-size:13px;line-height:15px;margin:8px 0 10px;width:250px}
.chat .btn{width:240px}
</style>
</head>
<body>
<div class="top-band"></div>
<div class="hero-photo" role="img" aria-label="Photo of a smiling young woman working at a laptop in a bright office"></div>

<nav class="nav">
  <a class="current">Home</a><a>Profile</a><a>Followers</a><a>My Uploads</a>
  <div class="account"><span>Login</span>|<span>Register</span></div>
  <div class="search"><input value="search" aria-label="search"><b>Go</b></div>
</nav>

<div class="brand"><i></i>WeatheredIt</div>

<div class="slogan">
  <h1>Learn from <strong>Experience</strong></h1>
  <p>Experience is the best teacher overall</p>
</div>
<div class="dots"><span></span><span></span><span></span><span></span><span></span></div>

<form class="ask">
  <h2>Ask your Question</h2>
  <p>and get answered by the experienced people around the world</p>
  <div class="field">Name</div>
  <div class="field">email address</div>
  <div class="field tall">your question</div>
  <div class="field">Select Quadrant</div>
  <div class="row"><div class="field">Upload Video (optional)</div><div class="field">Browse</div></div>
  <span class="btn">Get Answer</span>
</form>

<main class="content">
  <h2 class="section-title" style="left:15px;top:28px">Fresh Articles</h2>
  <div class="rule" style="left:40px;top:62px;width:480px"></div>
  <h2 class="section-title" style="left:528px;top:28px">Browse by Quadrant</h2>
  <div class="rule" style="left:528px;top:62px;width:360px"></div>

  <article class="article" style="top:78px"><h3>Problem in life with Money</h3><div class="meta">July 13, 2012<br>132 response, 8996 views</div><div class="share"><i></i><i></i><i></i><i></i><i></i><i></i></div><p>This is Draftwell's version &nbsp;of Lorem Ipsum. Proin gravida nibh vel velit auctor aliquet. Aenean sollicitudin, lorem quis bibendum auctor, nisi elit consequat ipsum, nec sagittis sem nibh id elit. Duis sed ...</p><span class="more">more</span></article>
  <article class="article" style="top:234px"><h3>Problem in life with Money</h3><div class="meta">July 13, 2012<br>132 response, 8996 views</div><div class="share"><i></i><i></i><i></i><i></i><i></i><i></i></div><p>This is Draftwell's version &nbsp;of Lorem Ipsum. Proin gravida nibh vel velit auctor aliquet. Aenean sollicitudin, lorem quis bibendum auctor, nisi elit consequat ipsum, nec sagittis sem nibh id elit. Duis sed ...</p><span class="more">more</span></article>
  <article class="article" style="top:389px"><h3>Problem in life with Money</h3><div class="meta">July 13, 2012<br>132 response, 8996 views</div><div class="share"><i></i><i></i><i></i><i></i><i></i><i></i></div><p>This is Draftwell's version &nbsp;of Lorem Ipsum. Proin gravida nibh vel velit auctor aliquet. Aenean sollicitudin, lorem quis bibendum auctor, nisi elit consequat ipsum, nec sagittis sem nibh id elit. Duis sed ...</p><span class="more">more</span></article>
  <article class="article" style="top:544px"><h3>Problem in life with Money</h3><div class="meta">July 13, 2012<br>132 response, 8996 views</div><div class="share"><i></i><i></i><i></i><i></i><i></i><i></i></div><p>This is Draftwell's version &nbsp;of Lorem Ipsum. Proin gravida nibh vel velit auctor aliquet. Aenean sollicitudin, lorem quis bibendum auctor, nisi elit consequat ipsum, nec sagittis sem nibh id elit. Duis sed ...</p><span class="more">more</span></article>

  <section class="quad" style="left:526px;top:84px"><h3>Financial Problems</h3>
    <div class="entry"><b>Problem in life with Money</b>July 13, 2012<br>132 response, 8996 views</div>
    <div class="entry"><b>Problem in life with Money</b>July 13, 2012<br>132 response, 8996 views</div>
    <div class="entry"><b>Problem in life with Money</b>July 13, 2012<br>132 response, 8996 views</div>
    <span class="more">more</span></section>
  <section class="quad" style="left:731px;top:84px"><h3>Legal Matters</h3>
    <div class="entry"><b>Problem in life with Money</b>July 13, 2012<br>132 response, 8996 views</div>
    <div class="entry"><b>Problem in life with Money</b>July 13, 2012<br>132 response, 8996 views</div>
    <div class="entry"><b>Problem in life with Money</b>July 13, 2012<br>132 response, 8996 views</div>
    <span class="more">more</span></section>
  <section class="quad" style="left:526px;top:323px"><h3>Medical &amp; Physical</h3>
    <div class="entry"><b>Problem in life with Money</b>July 13, 2012<br>132 response, 8996 views</div>
    <div class="entry"><b>Problem in life with Money</b>July 13, 2012<br>132 response, 8996 views</div>
    <div class="entry"><b>Problem in life with Money</b>July 13, 2012<br>132 response, 8996 views</div>
    <span class="more">more</span></section>
  <section class="quad" style="left:731px;top:323px"><h3>Psychological &amp;<br>Spiritual</h3>
    <div class="entry"><b>Problem in life with Money</b>July 13, 2012<br>132 response, 8996 views</div>
    <div class="entry"><b>Problem in life with Money</b>July 13, 2012<br>132 response, 8996 views</div>
    <span class="more">more</span></section>

  <div class="rule" style="left:550px;top:548px;width:360px"></div>
  <section class="chat">
    <h2>Chat Online with a<br>Life Coach</h2>
    <p>and get answered by the experienced people around the world</p>
    <span class="btn">Start Now</span>
  </section>
</main>
</body>
</html>
```